Flyer Design For Tech Support Company

We need a flyer design for our company Corvalo Tailored Device Services Ltd. I would like this to follow the same theme and styling of: www.corvalodevice.co.uk I would also invite you to use any information as found on our site. I would like this to focues primarily on attracting small bussines/start-up new custom; additionaly if there could be a mention of being able to work with private customers also.

Target Market(s)

Start-up, Small Businnes, Private Home.

Industry/Entity Type

It Company

Font styles to use
Sans Serif

Colors
33a6d7

Requirements
Must have
• Follow theme/style of main site.
• Be bold to attract from a distance.
Should not have
• Funny's

```html
<!DOCTYPE html>
<html lang="en">
<head>
<meta charset="utf-8">
<title>Corvalo Tailored Device Services – Flyer</title>
<link href="https://fonts.googleapis.com/css2?family=Bebas+Neue&family=Open+Sans:wght@400;600&display=swap" rel="stylesheet">
<style>
  :root {
    --brand: #33a6d7;
    --brand-deep: #2a8fc0;
    --ink: #1c1c1c;
    --paper: #f4f4f4;
    --paper-right: #ffffff;
    --backdrop: #e4e4e4;
    --photo-dark: #1d2a3a;
    --photo-light: #7fc6e6;
  }
  * { box-sizing: border-box; margin: 0; padding: 0; }
  html, body { width: 1200px; height: 1200px; overflow: hidden; }
  body {
    background: var(--backdrop);
    font-family: "Open Sans", sans-serif;
    color: var(--ink);
    position: relative;
  }
  .spread {
    position: absolute;
    left: 60px; top: 220px;
    width: 1080px; height: 760px;
    display: flex;
    box-shadow: 0 10px 30px rgba(0,0,0,0.12);
  }
  .page { width: 540px; height: 760px; position: relative; overflow: hidden; }

  /* Left page */
  .page-about { background: var(--paper); padding: 34px 40px 0; }
  .heading {
    font-family: "Bebas Neue", sans-serif;
    font-size: 38px; line-height: 1; text-align: center; letter-spacing: 0.5px;
  }
  .body-copy { font-size: 10.5px; line-height: 1.42; text-align: justify; }
  .intro { margin-top: 12px; }
  .intro p + p { margin-top: 0; }
  .founder { display: flex; gap: 18px; margin-top: 16px; }
  .founder-card { width: 160px; flex-shrink: 0; text-align: center; }
  .founder-photo { width: 150px; height: 150px; background: linear-gradient(160deg, #e9e9e9, #c9ccd1 55%, #2b2f36); margin: 0 auto; }
  .founder-caption { font-size: 10.5px; line-height: 1.35; margin-top: 6px; }
  .founder-story { flex: 1; }
  .services { margin-top: 16px; text-align: center; }
  .services .heading { font-size: 26px; }
  .service-list { list-style: none; font-size: 10.5px; line-height: 1.42; margin-top: 8px; }
  .partner-row {
    position: absolute; left: 40px; right: 40px; bottom: 28px;
    display: flex; align-items: flex-end; justify-content: space-between;
  }
  .partner-col { display: flex; flex-direction: column; align-items: center; gap: 10px; }
  .partner-name { font-size: 16px; font-weight: 600; color: #3a3a6e; }
  .social { display: flex; align-items: center; gap: 6px; font-size: 10.5px; font-weight: 600; color: #3b5b98; }
  .social-square { width: 22px; height: 22px; background: currentColor; }
  .social-chirper { color: var(--brand); }
  .footer-brand { text-align: center; }
  .footer-brand .brand-name { font-size: 18px; font-weight: 600; color: var(--brand); display: flex; align-items: center; gap: 6px; justify-content: center; }
  .brand-dot { width: 12px; height: 12px; border-radius: 50%; background: var(--brand); }
  .footer-brand .web { font-size: 12px; margin-top: 6px; }
  .cert-badge { width: 54px; height: 34px; background: #8a2a2a; border-radius: 4px; }

  /* Right page */
  .page-cover { background: var(--paper-right); }
  .cover-art { position: absolute; inset: 0; }
  .cover-brand {
    position: absolute; top: 70px; left: 0; right: 0;
    text-align: center; color: var(--brand);
    font-size: 30px; font-weight: 400; line-height: 1.15;
  }
  .cover-brand .brand-row { display: flex; align-items: center; justify-content: center; gap: 10px; }
  .cover-brand .brand-dot { width: 18px; height: 18px; }
  .cover-brand .brand-sub { font-size: 15px; letter-spacing: 1px; margin-top: 4px; }
  .tagline {
    position: absolute; right: 40px; bottom: 70px;
    font-family: "Bebas Neue", sans-serif;
    color: #fff; font-size: 32px; line-height: 1.05; text-align: right;
  }
</style>
</head>
<body>
<main class="spread">
  <section class="page page-about">
    <h2 class="heading">About Us</h2>
    <div class="body-copy intro">
      <p>Welcome to Corvalo Tailored Device Services Ltd, a professional company formed to meet your demands and exceed your expectations. From the smallest to the most complex technological need; from home computer troubleshooting to a custom designed and fitted tech solution – we are here to support you.</p>
      <p>Formed in 2015 to meet the ever-changing demands of our clients, to infuse our passion for technology with the on-going desire for supporting our clients' needs. We will take the formation of an idea, create a concept and work with our clients in realising that idea. At Corvalo, we realise that our clients' needs are ever changing and we look forward to supporting you every step of the way.</p>
    </div>
    <div class="founder">
      <figure class="founder-card">
        <div class="founder-photo" role="img" aria-label="Portrait photo of the company director, arms folded, in a dark branded polo shirt"></div>
        <figcaption class="founder-caption">Callum Reid<br>Director and Tech Specialist</figcaption>
      </figure>
      <p class="body-copy founder-story">Corvalo and our team was formed upon recognition of the lack of truly bespoke, all-inclusive tech support in the west of Scotland. I aim to remedy that! I have completed certified training with Maxivolt, Netrova and Crimsonix, three of the main players in the IT market. I have served with Albion Telecoms and ultimately 10 years with the Royal Fleet Service as a Radio and Communications Engineer, working on some of the most complex and advanced communications equipment available. I have a passion for Technology, one that has driven a career and a learning and development platform; a passion that I want to invest with you in making your tech needs happen.</p>
    </div>
    <div class="services">
      <h3 class="heading">Some of the services offered</h3>
      <ul class="service-list">
        <li>PC (Operating Fenestra, Orchard OS or Penguix) Software Rebuild and Troubleshoot.</li>
        <li>PC Hardware Troubleshoot or Upgrade.</li>
        <li>Home or Business Network (Wired or Wi-Fi) Installation or Troubleshoot.</li>
        <li>Telephone Extension Installation or Troubleshoot.</li>
        <li>Home Automation Installation e.g. Hearthly Remote Thermostat.</li>
        <li>Home or Business Backup Solutions.</li>
        <li>Home or Business Server Install, Configure or Secure.</li>
        <li>Home or Business IT/Tech Consultation Service.</li>
      </ul>
    </div>
    <div class="partner-row">
      <div class="partner-col">
        <span class="partner-name">Norvane Hosting</span>
        <span class="social"><span class="social-square"></span>Friendnet</span>
      </div>
      <div class="footer-brand">
        <div class="brand-name"><span class="brand-dot"></span>Corvalo</div>
        <div class="web">www.corvalodevice.co.uk</div>
      </div>
      <div class="partner-col">
        <span class="cert-badge" aria-label="Security certificate badge"></span>
        <span class="social social-chirper"><span class="social-square"></span>Chirper</span>
      </div>
    </div>
  </section>

  <section class="page page-cover">
    <svg class="cover-art" width="540" height="760" viewBox="0 0 540 760">
      <defs>
        <linearGradient id="photoTone" x1="0" y1="0" x2="1" y2="1">
          <stop offset="0" stop-color="var(--photo-light)"/>
          <stop offset="0.45" stop-color="#3d7fa8"/>
          <stop offset="1" stop-color="var(--photo-dark)"/>
        </linearGradient>
      </defs>
      <path role="img" aria-label="Photo of a businessman touching glowing hexagons labelled consulting, expert, knowledge and professional"
            d="M0,330 Q250,250 540,300 L540,560 Q330,650 0,545 Z" fill="url(#photoTone)"/>
      <path d="M0,545 Q330,650 540,560 L540,760 L0,760 Z" fill="var(--brand)"/>
    </svg>
    <div class="cover-brand">
      <div class="brand-row"><span class="brand-dot"></span>Corvalo</div>
      <div class="brand-sub">Tailored Device Services</div>
    </div>
    <p class="tagline">Providing a cost-effective consultation,<br>design and support service.</p>
  </section>
</main>
</body>
</html>
```